Create a bottle Label for Hadstrom American Vodka. LK Hadstrom’ Face (uploaded) should be prominent in the center of the label. The word “Hadstrom” should be above LK’s face and the words “American Vodka” under his face.

Target Market(s)

Buyers of Premium Vodka

Industry/Entity Type

Alcohol

Logo Text

Hadstrom American Vodka

Logo styles of interest
Pictorial/Combination Logo
Character Logo
Colors
00AB8E
00BBA5
67D7C9
C6EFE9
E9F9F6
FFF300
FFF600
FEFA6F
FFFEC7
FFFEE8
FFC000
F8CF3A
FAE287
FDF2CF
FEFAEE
F0912C
F2A743
F7CA91
FBE8D2
FDF5EE
EE7325
F08F49
F5BC92
FAE3D3
FDF4ED

Requirements
Must have
• LK Hadstrom face prominently displayed. The words “Hadstrom”. And “American Vodka”. LK Hadstrom signature.

```html
<!DOCTYPE html>
<html lang="en">
<head>
<meta charset="utf-8">
<title>Hadstrom American Vodka – Label</title>
<link href="https://fonts.googleapis.com/css2?family=Playfair+Display:wght@700&family=Saira+Semi+Condensed:wght@700&family=Yellowtail&display=swap" rel="stylesheet">
<style>
  :root {
    --ink: #4faa8f;
    --portrait-light: #cfe9e1;
    --portrait-deep: #7cc0aa;
    --paper: #ffffff;
    --backdrop: #f2f2f2;
  }
  * { margin: 0; padding: 0; box-sizing: border-box; }
  html, body {
    width: 1200px;
    height: 900px;
    overflow: hidden;
    background: var(--backdrop);
  }
  .canvas {
    position: relative;
    width: 1200px;
    height: 900px;
  }
  .label {
    position: absolute;
    left: 300px;
    top: 42px;
    width: 600px;
    height: 815px;
  }
  .label-frame, .label-shelf {
    fill: none;
    stroke: var(--ink);
    stroke-width: 16;
    stroke-linecap: round;
  }
  .label-frame { fill: var(--paper); }
  .brand-name {
    font-family: "Playfair Display", serif;
    font-weight: 700;
    fill: var(--ink);
  }
  .product-type {
    font-family: "Saira Semi Condensed", sans-serif;
    font-weight: 700;
    fill: var(--ink);
    letter-spacing: 2px;
  }
  .signature {
    font-family: "Yellowtail", cursive;
    fill: var(--ink);
  }
</style>
</head>
<body>
<main class="canvas">
  <svg class="label" viewBox="0 0 600 815" xmlns="http://www.w3.org/2000/svg">
    <defs>
      <radialGradient id="portraitTone" cx="50%" cy="45%" r="60%">
        <stop offset="0%" stop-color="var(--portrait-light)"/>
        <stop offset="100%" stop-color="var(--portrait-deep)"/>
      </radialGradient>
    </defs>

    <rect class="label-frame" x="8" y="8" width="584" height="799" rx="56"/>

    <text class="brand-name" x="50" y="210" font-size="175"
          textLength="500" lengthAdjust="spacingAndGlyphs">HADSTROM</text>

    <rect class="portrait" x="110" y="230" width="390" height="420" rx="160"
          fill="url(#portraitTone)" role="img"
          aria-label="Engraved-style portrait of LK Hadstrom in profile, bearded, wearing a suit"/>

    <text class="product-type" x="50" y="712" font-size="74"
          textLength="500" lengthAdjust="spacingAndGlyphs">AMERICAN VODKA</text>

    <path class="label-shelf" d="M16 700 Q16 752 60 752 H100"/>
    <path class="label-shelf" d="M500 752 H540 Q584 752 584 700"/>

    <text class="signature" x="300" y="766" font-size="42" text-anchor="middle">LK Hadstrom signature</text>
  </svg>
</main>
</body>
</html>
```